Sri Lankan Cricket Tour For Girls Aged 14-18 in July 2018

We need a flyer to promote a cricket tour of Sri Lanka in July 2018 for girls aged 14-18.
We want the flyer to call for "expressions of interest".
We would like the Sri Lankan Flag also images of cricket ball and beaches and palm trees etc.
Mention Level 3 Coaches with International experience.
Target market is parents of girls aged 14 to 18 and girls aged 14 to 18

Target Market(s)

Parents of girls aged 14 to 18 and girls aged 14 to 18

Industry/Entity Type

Travel

Font styles to use
Serif
Sans Serif

Colors
0355a3
ec1f27
fbed22

Requirements
Must have
• Sri Lankan Flag, Halvey Athletics Logo, email address boyd@halveyathletics.com.au.
• - 10 Day Tour
• - Play on First Class Grounds
• - Level 3 Coaches With International Experience
• - For More Information Contact Boyd boyd@halveyathletics.com.au
Nice to have
• Picture of girls playing cricket, sun and beach
Should not have
• Cartoon type images
• Photo's of actual cricketers

```html
<!DOCTYPE html>
<html lang="en">
<head>
<meta charset="utf-8">
<title>Cricket Tour of Sri Lanka for Girls – Halvey Athletics</title>
<link rel="stylesheet" href="https://fonts.googleapis.com/css2?family=Orbitron:wght@700;900&family=Montserrat:wght@700;800&display=swap">
<style>
  :root {
    --backdrop: #a7a9ac;
    --ink-black: #111214;
    --brand-blue: #0355a3;
    --sky-blue: #1e74c9;
    --sea-cyan: #4cc3e6;
    --sand: #e9e4d2;
    --palm-green: #2f6b2a;
    --brand-red: #ec1f27;
    --band-red: #8c1118;
    --brand-yellow: #fbed22;
    --white: #ffffff;
    --grass: #5c8a3a;
    --flag-maroon: #8d153a;
    --flag-green: #00534e;
    --flag-orange: #eb7400;
    --flag-gold: #ffbe29;
  }
  * { margin: 0; padding: 0; box-sizing: border-box; }
  html, body {
    width: 801px; height: 1200px; overflow: hidden;
    background: var(--backdrop);
  }
  .flyer {
    position: absolute; left: 30px; top: 122px;
    width: 740px; height: 956px;
    background: var(--white);
    overflow: hidden;
    box-shadow: 4px 6px 10px rgba(0,0,0,0.35);
    font-family: "Montserrat", sans-serif;
  }
  .beach-scene {
    position: absolute; left: 0; top: 150px; width: 740px; height: 405px;
    background:
      radial-gradient(ellipse 260px 300px at 90px 150px, rgba(47,107,42,0.85), rgba(47,107,42,0) 70%),
      linear-gradient(180deg, var(--brand-blue) 0%, var(--sky-blue) 45%, var(--sea-cyan) 78%, var(--sand) 92%, var(--sand) 100%);
  }
  .header-band { position: absolute; left: 0; top: 0; width: 740px; height: 230px; }
  .brand {
    position: absolute; left: 48px; top: 56px; width: 240px;
    text-align: center;
  }
  .brand-mark {
    display: block; width: 84px; height: 84px; margin: 0 auto 12px;
    border-radius: 50%; background: var(--brand-red);
  }
  .brand-name {
    font-family: "Orbitron", sans-serif; font-weight: 700;
    font-size: 18px; letter-spacing: 1px; text-transform: uppercase;
    color: var(--brand-red);
  }
  .call-to-action {
    position: absolute; left: 300px; top: 50px; width: 420px;
    font-family: "Orbitron", sans-serif; font-weight: 900;
    font-size: 40px; line-height: 62px; color: var(--brand-yellow);
    text-align: center; letter-spacing: 1px;
  }
  .flag {
    position: absolute; left: 510px; top: 172px; width: 190px; height: 140px;
    transform: rotate(-8deg);
    filter: drop-shadow(3px 4px 4px rgba(0,0,0,0.4));
  }
  .tour-title {
    position: absolute; right: 34px; top: 330px;
    font-family: "Orbitron", sans-serif; font-weight: 900;
    color: var(--white); text-align: right;
    text-shadow: 2px 2px 3px rgba(0,0,0,0.45);
  }
  .tour-title .line { display: block; font-size: 37px; line-height: 54px; }
  .tour-title .line--feature { font-size: 54px; line-height: 66px; }
  .tour-title .line--age { font-size: 40px; line-height: 56px; }
  .date-badge { position: absolute; left: -4px; top: 470px; width: 152px; height: 100px; }
  .date-badge text {
    font-family: "Orbitron", sans-serif; font-weight: 900; font-size: 15px;
    fill: var(--white);
  }
  .highlights {
    position: absolute; left: 0; top: 555px; width: 740px; height: 116px;
    background: linear-gradient(180deg, #a3151d 0%, var(--band-red) 100%);
    padding: 18px 0 0 30px; list-style: none;
  }
  .highlights li {
    color: var(--white); font-weight: 800; font-size: 19px;
    line-height: 26.5px; text-transform: uppercase; letter-spacing: 0.5px;
  }
  .highlights li::before {
    content: ""; display: inline-block; width: 9px; height: 9px;
    border-radius: 50%; background: var(--white);
    margin: 0 14px 3px 0; vertical-align: middle;
  }
  .gallery {
    position: absolute; left: 35px; top: 710px; width: 678px; height: 130px;
    display: flex; justify-content: space-between;
  }
  .gallery-photo {
    width: 214px; height: 130px;
    border: 3px solid var(--brand-red);
    box-shadow: 2px 3px 5px rgba(0,0,0,0.35);
    background: linear-gradient(180deg, #3f5e2e 0%, #6c9946 55%, var(--grass) 100%);
  }
  .divider { position: absolute; left: 0; top: 872px; width: 740px; height: 5px; background: var(--brand-red); }
  .contact {
    position: absolute; left: 0; top: 877px; width: 740px; height: 79px;
    background: var(--brand-blue); color: var(--white); text-align: center;
    padding-top: 15px;
  }
  .contact-label { font-weight: 700; font-size: 15px; letter-spacing: 0.6px; text-transform: uppercase; }
  .contact-email { font-weight: 800; font-size: 22px; letter-spacing: 0.5px; text-transform: uppercase; margin-top: 2px; }
</style>
</head>
<body>
<main class="flyer">
  <div class="beach-scene" role="img" aria-label="Tropical beach with palm trees, blue sky and sea"></div>

  <svg class="header-band" viewBox="0 0 740 230" aria-hidden="true">
    <path d="M0 0 H740 V175 C640 150 560 212 420 200 C300 188 200 200 120 214 C60 224 20 214 0 204 Z" fill="var(--ink-black)"/>
  </svg>

  <div class="brand">
    <span class="brand-mark"></span>
    <span class="brand-name">Halvey Athletics</span>
  </div>

  <h2 class="call-to-action">EXPRESSIONS<br>OF INTEREST</h2>

  <svg class="flag" viewBox="0 0 190 140" role="img" aria-label="Flag of Sri Lanka">
    <rect x="0" y="0" width="190" height="140" fill="var(--flag-gold)"/>
    <rect x="10" y="10" width="30" height="120" fill="var(--flag-green)"/>
    <rect x="40" y="10" width="30" height="120" fill="var(--flag-orange)"/>
    <rect x="80" y="10" width="100" height="120" fill="var(--flag-maroon)"/>
  </svg>

  <h1 class="tour-title">
    <span class="line">Cricket Tour</span>
    <span class="line">Of Sri Lanka</span>
    <span class="line line--feature">For Girls</span>
    <span class="line line--age">Aged 14 - 18</span>
  </h1>

  <svg class="date-badge" viewBox="0 0 100 66" aria-label="July 2018">
    <polygon fill="var(--brand-red)" stroke="var(--brand-yellow)" stroke-width="1.5"
      points="100,33 92.5,40.3 93.3,49.5 81.1,52.8 75,61.6 61.4,60 50,66 38.6,60 25,61.6 18.9,52.8 6.7,49.5 7.5,40.3 0,33 7.5,25.7 6.7,16.5 18.9,13.2 25,4.4 38.6,6 50,0 61.4,6 75,4.4 81.1,13.2 93.3,16.5 92.5,25.7"/>
    <text x="46" y="30" text-anchor="middle">July</text>
    <text x="48" y="49" text-anchor="middle">2018</text>
  </svg>

  <ul class="highlights">
    <li>First Class Grounds</li>
    <li>10 Day Tour</li>
    <li>Level 3 Coaches With International Experience</li>
  </ul>

  <div class="gallery">
    <div class="gallery-photo" role="img" aria-label="Girl batting on a cricket ground with wicketkeeper behind"></div>
    <div class="gallery-photo" role="img" aria-label="Young batter playing a shot at the crease"></div>
    <div class="gallery-photo" role="img" aria-label="Group of girls in cricket whites celebrating"></div>
  </div>

  <div class="divider"></div>

  <footer class="contact">
    <p class="contact-label">For more information contact</p>
    <p class="contact-email">boyd@halveyathletics.com.au</p>
  </footer>
</main>
</body>
</html>
```